Comets Business Card Design Project

Create a standard format for letterhead and business cards. I know I can just get the layout with an example name on it, then add the names, titles and address that we want to it and give that to a printer so that the graphics are much better. Organization Mission Statement: Providing a professionally organized, structured, and supportive environment with quality development and professional coaching to inspire our student athletes, and assist them in fulfilling their dreams of achievement in academic excellence, high level competition and playing collegiate softball. Girl's Elite Fastpitch Softball

Check web site: www.brookvalediamondcomets.org
Updates

Sorry I didn't get the URL and files out when I started the project. Logo examples, mission, vision, etc. are posted now. And the URL to the web site is www.brookvalediamondcomets.org.

I'm very interested in an original creative design that is professional yet relevant to a sports team and for coaches.

Target Market(s)

college recuriters, industry product suppliers, parents, coaches, tournament directors

Industry/Entity Type

Environment

Requirements
Must have
• Use one of two logos; include the web site URL and a general mailbox for inquires. Includes Name, title, email and phone number
Nice to have
• Some color variations or background. Maybe a mission statement on the back. Maybe a QR code to the web site.

```html
<!DOCTYPE html>
<html lang="en">
<head>
<meta charset="utf-8">
<title>Brookvale Diamond Comets – Business Card</title>
<link rel="stylesheet" href="https://fonts.googleapis.com/css2?family=EB+Garamond:wght@400&family=Arimo:wght@400&family=Kaushan+Script&display=swap">
<style>
  :root {
    --canvas: #ffffff;
    --card-edge: #8a8a8a;
    --team-red: #c0253e;
    --soft-tint: #f7e3e7;
    --ink: #1d1a1a;
    --band-text: #ffffff;
    --asterisk: #f1c9d0;
  }
  * { margin: 0; padding: 0; box-sizing: border-box; }
  html, body { width: 1200px; height: 901px; overflow: hidden; background: var(--canvas); }
  .canvas { position: relative; width: 1200px; height: 901px; }

  .card {
    position: absolute; width: 641px; height: 356px;
    border: 1px solid var(--card-edge); background: var(--canvas); overflow: hidden;
  }
  .card--front { left: 117px; top: 81px; }
  .card--back { left: 465px; top: 502px; }

  .card__backdrop { position: absolute; inset: 0; }
  .card--front .card__backdrop {
    background: radial-gradient(ellipse 190px 170px at 160px 190px, var(--soft-tint) 0%, rgba(247,227,231,0) 100%);
  }
  .card--back .card__backdrop {
    background:
      radial-gradient(ellipse 170px 150px at 165px 160px, var(--soft-tint) 0%, rgba(247,227,231,0) 100%),
      radial-gradient(ellipse 110px 110px at 460px 225px, var(--soft-tint) 0%, rgba(247,227,231,0) 100%);
  }

  .serif { font-family: "EB Garamond", Garamond, serif; }
  .sans { font-family: "Arimo", Arial, sans-serif; }
  .abs { position: absolute; white-space: nowrap; line-height: 1; font-weight: 400; }

  /* front */
  .team-band {
    position: absolute; left: 11px; top: 21px; width: 617px; height: 92px;
    background: var(--team-red); color: var(--band-text);
  }
  .team-band__asterisks { color: var(--asterisk); font-size: 13px; letter-spacing: 3px; }
  .team-band__mark { font-size: 27px; left: 66px; top: 32px; }
  .team-band__mark::before {
    content: ""; display: inline-block; width: 10px; height: 10px;
    background: var(--band-text); margin-right: 8px; vertical-align: middle;
  }
  .team-band__name { font-size: 22.7px; left: 236px; top: 19px; }
  .team-band__tagline { font-size: 25px; left: 266px; top: 59px; }

  .person__name {
    font-family: "Kaushan Script", "Brush Script MT", cursive;
    font-weight: 400; font-size: 40px; color: var(--ink); left: 188px; top: 120px;
  }
  .person__title { font-size: 21px; color: var(--ink); left: 177px; line-height: 29px; top: 169px; white-space: normal; width: 360px; }
  .contact { font-size: 18px; color: var(--ink); }
  .contact__label { left: 191px; }
  .contact__value { left: 254px; letter-spacing: 1.6px; }
  .web { font-size: 16.5px; color: var(--ink); }

  /* back */
  .mission {
    position: absolute; left: 96px; top: 58px; width: 520px;
    font-size: 24.2px; line-height: 28.7px; color: var(--team-red);
  }
  .mailbox { font-size: 23px; color: var(--team-red); left: 170px; top: 296px; }
</style>
</head>
<body>
<div class="canvas">
  <section class="card card--front">
    <div class="card__backdrop" role="img" aria-label="Faint pink decorative backdrop"></div>

    <header class="team-band">
      <span class="abs team-band__asterisks" style="left:5px;top:50px">*****</span>
      <span class="abs serif team-band__mark">Brookvale</span>
      <span class="abs sans team-band__name">BROOKVALE DIAMOND COMETS</span>
      <span class="abs team-band__asterisks" style="left:222px;top:50px">************************************</span>
      <span class="abs serif team-band__tagline">Girl's Elite Fastpitch Softball</span>
    </header>

    <h1 class="abs person__name">Marcus Hale</h1>
    <p class="abs serif person__title">Board Member, Softball Operations,<br>Player Recruiting, Team Manager</p>

    <span class="abs serif contact contact__label" style="top:238px">Tel:</span>
    <span class="abs serif contact contact__value" style="top:238px">999999999999999999</span>
    <span class="abs serif contact contact__label" style="top:265px">Mob:</span>
    <span class="abs serif contact contact__value" style="top:265px">888888888888888888</span>

    <span class="abs serif web" style="left:36px;top:296px">marcus@brookvalediamondcomets.org</span>
    <span class="abs serif web" style="left:340px;top:296px">www.profilehub.net/in/marcushale</span>
    <span class="abs serif web" style="left:190px;top:321px">www.brookvalediamondcomets.org</span>
  </section>

  <section class="card card--back">
    <div class="card__backdrop" role="img" aria-label="Faint pink decorative backdrop"></div>

    <p class="sans mission">Providing a professionally organized,<br>structured, and supportive environment<br>with quality development and professional<br>coaching to inspire our student athletes,<br>and assist them in fulfilling their dreams of<br>achievement in academic excellence,<br>high level competition and playing<br>collegiate softball</p>
    <span class="abs serif mailbox">tryouts@brookvalediamondcomets.org</span>
  </section>
</div>
</body>
</html>
```